Criação de Papelaria Profissional para Construção & Engenharia
" Empresa que atua em incorporação imobiliária, administrando a construção de edifícios "

```html
<!DOCTYPE html>
<html lang="pt-BR">
<head>
<meta charset="UTF-8">
<title>Envelope — Tavares Lima</title>
<link href="https://fonts.googleapis.com/css2?family=Montserrat:wght@400;500&display=swap" rel="stylesheet">
<style>
  :root{
    --navy:#1f4d8f;
    --navy-deep:#183f78;
    --silver:#c9ccd1;
    --silver-light:#eef0f3;
    --paper:#ffffff;
    --backdrop:#e6e7e9;
    --ink:#6f747b;
  }
  *{margin:0;padding:0;box-sizing:border-box}
  html,body{width:1200px;height:1200px;overflow:hidden}
  body{background:var(--backdrop);font-family:"Montserrat",sans-serif;position:relative}

  .envelope{position:absolute;left:192px;width:816px;box-shadow:0 6px 18px rgba(0,0,0,.18)}

  .envelope--back{top:132px;height:415px;background:var(--navy)}
  .envelope--back .silver-stripe{position:absolute;left:0;right:0;top:380px;height:11px;
    background:linear-gradient(90deg,var(--silver),var(--silver-light) 45%,var(--silver))}
  .envelope--back .brand{position:absolute;left:50%;top:175px;transform:translateX(-50%)}
  .envelope--back .brand__mark{background:var(--silver-light)}
  .envelope--back .brand__name{color:var(--silver-light)}

  .envelope--front{top:583px;height:413px;background:var(--paper)}
  .flap{position:absolute;left:0;top:0;width:816px;height:115px}
  .envelope--front .brand{position:absolute;left:50%;top:185px;transform:translateX(-50%)}
  .envelope--front .brand__mark{background:var(--navy)}
  .envelope--front .brand__name{color:var(--navy)}

  .brand{display:flex;align-items:center;gap:26px;white-space:nowrap}
  .brand__mark{width:86px;height:86px}
  .brand__name{font-size:42px;font-weight:500;letter-spacing:2px}

  .contacts{position:absolute;left:0;right:0;top:360px;display:flex;justify-content:center;gap:26px;
    font-size:12.5px;color:var(--ink);list-style:none}
  .contacts li{display:flex;align-items:center;gap:8px;line-height:1.25}
  .contacts svg{width:16px;height:16px;flex:none}
  .dot{width:14px;height:14px;border-radius:50%;border:1.6px solid var(--ink);flex:none}
</style>
</head>
<body>

<section class="envelope envelope--back" aria-label="Envelope, verso">
  <div class="brand">
    <span class="brand__mark"></span>
    <span class="brand__name">TAVARES LIMA</span>
  </div>
  <div class="silver-stripe"></div>
</section>

<section class="envelope envelope--front" aria-label="Envelope, frente">
  <svg class="flap" viewBox="0 0 816 115" aria-hidden="true">
    <path d="M0 0 H816 V12 L745 100 Q736 112 720 112 H96 Q80 112 71 100 L0 12 Z" fill="var(--navy)"/>
  </svg>
  <div class="brand">
    <span class="brand__mark"></span>
    <span class="brand__name">TAVARES LIMA</span>
  </div>
  <ul class="contacts">
    <li>
      <svg viewBox="0 0 16 16"><path d="M4 2l2.5 3-1.5 1.5c.8 1.8 2.2 3.2 4 4L10.5 9 13.5 11.5 12 14C7 14 2 9 2 4z" fill="none" stroke="var(--ink)" stroke-width="1.3" stroke-linejoin="round"/></svg>
      (12) 9000-4417
    </li>
    <li>
      <svg viewBox="0 0 16 16"><rect x="1.5" y="3.5" width="13" height="9" rx="1" fill="none" stroke="var(--ink)" stroke-width="1.3"/><path d="M2 4l6 5 6-5" fill="none" stroke="var(--ink)" stroke-width="1.3"/></svg>
      contato@tavareslima.com.br
    </li>
    <li><span class="dot"></span>/tavareslimaeng</li>
    <li><span class="dot"></span>@tavareslima</li>
    <li>
      <svg viewBox="0 0 16 16"><path d="M8 15s-5-5.5-5-9a5 5 0 0110 0c0 3.5-5 9-5 9z" fill="none" stroke="var(--ink)" stroke-width="1.3"/><circle cx="8" cy="6" r="1.8" fill="var(--ink)"/></svg>
      <span>R. das Acácias, 48<br>Ubatuba SP</span>
    </li>
  </ul>
</section>

</body>
</html>
```